Women's Health Company needs business card

We need a business card for a USA based women's health care company. We use digital technology to enhance therapy prescribed by clinicians for their patients

```html
<!DOCTYPE html>
<html lang="en">
<head>
<meta charset="utf-8">
<title>Corvela Health – Business Card</title>
<link rel="stylesheet" href="https://fonts.googleapis.com/css2?family=Open+Sans:wght@400;600;700&display=swap">
<style>
  :root {
    --backdrop: #4a4a4a;
    --card: #ffffff;
    --teal: #76bfbb;
    --purple: #8d52a1;
    --ink: #1f1f1f;
  }
  * { box-sizing: border-box; margin: 0; padding: 0; }
  html, body {
    width: 1200px;
    height: 801px;
    overflow: hidden;
  }
  body {
    background: var(--backdrop);
    font-family: "Open Sans", Arial, sans-serif;
    position: relative;
  }
  .card {
    position: absolute;
    top: 246px;
    width: 540px;
    height: 309px;
    background: var(--card);
    border-bottom: 3px solid var(--teal);
  }
  .card--front { left: 40px; }
  .card--back { left: 620px; }

  .brand {
    display: flex;
    align-items: center;
    gap: 10px;
    color: var(--teal);
    font-weight: 600;
    white-space: nowrap;
  }
  .brand__dot {
    border-radius: 50%;
    background: var(--purple);
    flex: none;
  }

  /* front side */
  .card--front .brand {
    position: absolute;
    left: 34px;
    top: 132px;
    font-size: 30px;
  }
  .card--front .brand__dot { width: 11px; height: 11px; }
  .divider {
    position: absolute;
    left: 272px;
    top: 58px;
    width: 2px;
    height: 192px;
    background: var(--teal);
  }
  .contact {
    position: absolute;
    left: 296px;
    top: 62px;
    color: var(--ink);
    font-size: 12.5px;
    line-height: 1.45;
  }
  .contact__name {
    color: var(--teal);
    font-weight: 700;
    font-size: 17px;
    letter-spacing: 0.5px;
    text-transform: uppercase;
    line-height: 1.2;
  }
  .contact__title { font-size: 13px; margin-bottom: 14px; }
  .contact__address { margin-bottom: 14px; }
  .contact__line {
    display: flex;
    align-items: center;
    gap: 7px;
  }
  .contact__icon { width: 12px; height: 12px; flex: none; }

  /* back side */
  .card--back .brand {
    position: absolute;
    left: 50%;
    top: 50%;
    transform: translate(-50%, -50%);
    font-size: 48px;
    gap: 14px;
  }
  .card--back .brand__dot { width: 16px; height: 16px; }
</style>
</head>
<body>

  <section class="card card--front" aria-label="Business card, contact side">
    <div class="brand">
      <span class="brand__dot"></span>
      <span class="brand__name">Corvela Health</span>
    </div>

    <div class="divider"></div>

    <div class="contact">
      <p class="contact__name">Lena Marlowe</p>
      <p class="contact__title">President</p>
      <p class="contact__address">4172 Seabright Lane<br>Oceanside CA 92054</p>
      <p class="contact__line">
        <svg class="contact__icon" viewBox="0 0 12 12" aria-hidden="true">
          <circle cx="6" cy="6" r="6" fill="#76bfbb"/>
          <path d="M3.6 3.2l1.3-.4.8 1.6-.8.6c.3.8.9 1.4 1.7 1.7l.6-.8 1.6.8-.4 1.3C6.5 8.3 3.7 5.5 3.6 3.2z" fill="#fff"/>
        </svg>
        555 014 2237
      </p>
      <p class="contact__line">
        <svg class="contact__icon" viewBox="0 0 12 12" aria-hidden="true">
          <rect x="0.5" y="2" width="11" height="8" rx="1" fill="#76bfbb"/>
          <path d="M1 2.6l5 3.6 5-3.6" stroke="#fff" stroke-width="1" fill="none"/>
        </svg>
        hello@corvelahealth.com
      </p>
      <p class="contact__line">
        <svg class="contact__icon" viewBox="0 0 12 12" aria-hidden="true">
          <circle cx="6" cy="6" r="6" fill="#76bfbb"/>
          <ellipse cx="6" cy="6" rx="2.4" ry="4.6" stroke="#fff" stroke-width="0.9" fill="none"/>
          <path d="M1.4 6h9.2" stroke="#fff" stroke-width="0.9"/>
        </svg>
        www.corvelahealth.com
      </p>
    </div>
  </section>

  <section class="card card--back" aria-label="Business card, brand side">
    <div class="brand">
      <span class="brand__dot"></span>
      <span class="brand__name">Corvela Health</span>
    </div>
  </section>

</body>
</html>
```